Mobile Friendly Lead Generation Landing Page

We are a web marketing company that specialized in web lead generation. Recently we have started buying media from mobile devices and we need a mobile interface(landing page) where we can collect user data in an effective manner.

Our current mobile landing page is:
http://www.pathwaylocate.example.com/lp13d/index.aspx?a=true&source=591483
Through this you can see what the steps/questions users need to answer to get matched to a school. We need the design for the whole process.

We are pretty open for design ideas and our goal is to make this mobile optimized landing page have the look and feel of an app...but not an app.
There are several questions in the process but we are open to changing the way they are presented. As in, you can have one question at a time or a few.
The goal is to make this EXTREMELY EASY for users to interact with.

One example that we have liked is:
http://tutorhubnet.example.com/schools/72615-page1.thub (please note that this opens only on mobile devices)

Some of these screenshots are attached.

Our web form looks like this:
http://www.pathwaylocate.example.com/lp88/index.aspx?a=true

```html
<!DOCTYPE html>
<html lang="en">
<head>
<meta charset="utf-8">
<title>PathwayLocate – Field of interest step</title>
<link rel="stylesheet" href="https://fonts.googleapis.com/css2?family=Roboto:wght@400;500;700&display=swap">
<style>
  :root {
    --page-bg: #f1f3f5;
    --brand-blue: #13aee0;
    --brand-blue-dark: #0d8fc0;
    --sky-top: #d3ebf8;
    --sky-mid: #e2f1fa;
    --hill-green: #5cbf2a;
    --ribbon-green: #7ed321;
    --ribbon-green-dark: #5aa818;
    --ribbon-fold: #3f7d0f;
    --night-top: #232b30;
    --night-bottom: #283237;
    --text-dark: #1f2a30;
    --text-light: #ffffff;
    --count-blue: #13aee0;
    --count-blue-night: #3cc3f0;
  }
  * { box-sizing: border-box; margin: 0; padding: 0; }
  html, body {
    width: 1200px; height: 1000px; overflow: hidden;
    background: var(--page-bg);
    font-family: "Roboto", Arial, sans-serif;
  }
  .canvas { position: relative; width: 1200px; height: 1000px; }

  .screen {
    position: absolute; top: 158px;
    width: 380px; height: 670px;
    overflow: hidden;
  }
  .screen--day { left: 153px; }
  .screen--night { left: 676px; }

  .backdrop { position: absolute; inset: 0; }
  .screen--day .backdrop {
    background: linear-gradient(to bottom,
      var(--sky-top) 0%, var(--sky-mid) 62%,
      #c9d9dd 72%, #8fcf5a 80%, var(--hill-green) 100%);
  }
  .screen--night .backdrop {
    background: linear-gradient(to bottom, var(--night-top), var(--night-bottom));
  }

  .app-header {
    position: absolute; top: 0; left: 0; right: 0; height: 66px;
    display: flex; align-items: center; justify-content: center; gap: 9px;
  }
  .screen--day .app-header { background: var(--brand-blue); }
  .screen--night .app-header { top: 10px; }
  .brand-dot {
    width: 26px; height: 26px; border-radius: 50%;
    background: var(--text-light);
  }
  .brand-name {
    font-size: 29px; font-weight: 700; color: var(--text-light);
    letter-spacing: -0.3px;
  }

  .progress { position: absolute; top: 88px; left: 0; width: 380px; height: 120px; }
  .progress svg { position: absolute; inset: 0; }
  .ribbon-label {
    position: absolute; top: 3px; left: 47px; width: 285px; height: 43px;
    display: flex; align-items: center; justify-content: center; gap: 9px;
    color: var(--text-light); font-size: 17.5px; font-weight: 400;
  }
  .ribbon-label strong { font-weight: 700; }
  .badge-label {
    position: absolute; top: 52px; left: 153px; width: 77px;
    text-align: center; color: var(--text-light); line-height: 1;
  }
  .badge-label .percent { display: block; font-size: 18px; font-weight: 700; }
  .badge-label .caption { display: block; font-size: 12px; margin-top: 3px; }

  .question {
    position: absolute; top: 223px; left: 24px; right: 0;
    font-size: 17px; color: var(--text-dark);
  }
  .screen--night .question { color: var(--text-light); }
  .question .step { font-weight: 700; color: var(--count-blue); margin-right: 6px; }
  .screen--night .question .step { color: var(--count-blue-night); }

  .choices { position: absolute; top: 260px; left: 17px; width: 343px; list-style: none; }
  .choice {
    height: 46px; margin-bottom: 10px; border-radius: 4px;
    background: var(--brand-blue); color: var(--text-light);
    font-size: 18px; display: flex; align-items: center; justify-content: center;
    position: relative;
  }
  .choice--other { background: var(--text-light); }
  .screen--day .choice--other { color: var(--brand-blue); border: 1px solid var(--brand-blue); }
  .screen--night .choice--other { color: var(--text-dark); }
  .choice-arrow { position: absolute; right: 14px; top: 14px; }

  .back-button {
    position: absolute; top: 604px; left: 17px; width: 343px; height: 46px;
    border-radius: 4px; background: var(--brand-blue);
    border: 1px solid rgba(255,255,255,0.85);
    color: var(--text-light); font-size: 19px; font-weight: 700;
    display: flex; align-items: center; justify-content: center;
  }
</style>
</head>
<body>
<main class="canvas">

  <section class="screen screen--day">
    <div class="backdrop" role="img" aria-label="Illustration of a light blue sky with clouds, grey snowy mountains, a yellow sun, pine trees, a small pond and green hills"></div>
    <header class="app-header">
      <span class="brand-dot"></span>
      <span class="brand-name">PathwayLocate</span>
    </header>
    <div class="progress">
      <svg width="380" height="120" viewBox="0 0 380 120">
        <polygon points="17,17 62,17 62,60 17,60 30,38" fill="var(--ribbon-green-dark)"/>
        <polygon points="363,17 318,17 318,60 363,60 350,38" fill="var(--ribbon-green-dark)"/>
        <polygon points="47,46 62,46 62,60" fill="var(--ribbon-fold)"/>
        <polygon points="333,46 318,46 318,60" fill="var(--ribbon-fold)"/>
        <path d="M153 46 H230 V100 L191.5 118 L153 100 Z" fill="var(--brand-blue-dark)"/>
        <path d="M157 46 H226 V97 L191.5 113 L157 97 Z" fill="var(--brand-blue)" stroke="rgba(255,255,255,0.5)" stroke-width="1"/>
        <rect x="47" y="3" width="286" height="43" fill="var(--ribbon-green)"/>
      </svg>
      <div class="ribbon-label">
        <span>Get matched in <strong>2 minutes</strong></span>
        <svg width="20" height="20" viewBox="0 0 20 20" aria-hidden="true">
          <circle cx="10" cy="10" r="8.5" fill="none" stroke="#fff" stroke-width="2"/>
          <path d="M10 5 V10 H14" fill="none" stroke="#fff" stroke-width="2"/>
        </svg>
      </div>
      <div class="badge-label"><span class="percent">0%</span><span class="caption">complete</span></div>
    </div>
    <p class="question"><span class="step">1/10</span>Please select your field of interest</p>
    <ul class="choices">
      <li class="choice">Art &amp; Design</li>
      <li class="choice">Business</li>
      <li class="choice">Business</li>
      <li class="choice choice--other">Other
        <svg class="choice-arrow" width="12" height="18" viewBox="0 0 12 18" aria-hidden="true"><path d="M2 2 L9 9 L2 16" fill="none" stroke="currentColor" stroke-width="2.5"/></svg>
      </li>
    </ul>
    <div class="back-button">Back</div>
  </section>

  <section class="screen screen--night">
    <div class="backdrop" role="img" aria-label="Illustration of a dark night sky with small stars and faint clouds"></div>
    <header class="app-header">
      <span class="brand-dot"></span>
      <span class="brand-name">PathwayLocate</span>
    </header>
    <div class="progress">
      <svg width="380" height="120" viewBox="0 0 380 120">
        <polygon points="17,17 62,17 62,60 17,60 30,38" fill="var(--ribbon-green-dark)"/>
        <polygon points="363,17 318,17 318,60 363,60 350,38" fill="var(--ribbon-green-dark)"/>
        <polygon points="47,46 62,46 62,60" fill="var(--ribbon-fold)"/>
        <polygon points="333,46 318,46 318,60" fill="var(--ribbon-fold)"/>
        <path d="M153 46 H230 V100 L191.5 118 L153 100 Z" fill="var(--brand-blue-dark)"/>
        <path d="M157 46 H226 V97 L191.5 113 L157 97 Z" fill="var(--brand-blue)" stroke="rgba(255,255,255,0.5)" stroke-width="1"/>
        <rect x="47" y="3" width="286" height="43" fill="var(--ribbon-green)"/>
      </svg>
      <div class="ribbon-label">
        <span>Get matched in <strong>2 minutes</strong></span>
        <svg width="20" height="20" viewBox="0 0 20 20" aria-hidden="true">
          <circle cx="10" cy="10" r="8.5" fill="none" stroke="#fff" stroke-width="2"/>
          <path d="M10 5 V10 H14" fill="none" stroke="#fff" stroke-width="2"/>
        </svg>
      </div>
      <div class="badge-label"><span class="percent">70%</span><span class="caption">complete</span></div>
    </div>
    <p class="question"><span class="step">1/10</span>Please select your field of interest</p>
    <ul class="choices">
      <li class="choice">Art &amp; Design</li>
      <li class="choice">Business</li>
      <li class="choice">Business</li>
      <li class="choice choice--other">Other
        <svg class="choice-arrow" width="12" height="18" viewBox="0 0 12 18" aria-hidden="true"><path d="M2 2 L9 9 L2 16" fill="none" stroke="currentColor" stroke-width="2.5"/></svg>
      </li>
    </ul>
    <div class="back-button">Back</div>
  </section>

</main>
</body>
</html>
```